Steady Yield Spread Tactics for hurried readers

"Necessity is the mother of invention"

The idea of vetting investment strategies is not new in the financial world before investing real monies. Vetting strategies in options strategies always have been a difficult exercise. Such exercise requires access to programmers, right tools and good historical data. These factors make vetting process very costly and tedious. Becuase of this reason, this process is mostly limited to hedge funds, private banking, wealth management firms. Very few products existed in the market to support this process.

Since my graduation in engineering with major in Computer Science, I worked in large global banks as an IT consultant. Over there, I was designing, developing or managing large IT projects. This job profile demanded long hours, busy and tiring days. Very few hours or literally, not enough time available to analyze investment opportunities.

Moreover, investing in stocks without understanding valuation, business model and financials of the companies often result in losses. More so, if not enough understanding on when to exit from a position. Entering into a position is easy and it is in trader's control but exiting a position when profiting and cutting losses is an important step to make money consistently. This needed more disciplined approach and defined rules for position sizing, money management, profit taking and cutting losses.

Options have greeks that will affect its pricing. Understanding and leading options is another major step in the hurdle of investing in options. There are good mentors/experts teaching options. Gaining conceptual understanding is not that difficult. Practically seeing the market affecting the options trades is the most difficult step. Mentors/experts use primitive tools that give some peek into the practical process but it is very tedious since they often provide manual backtesting. "Options" provide options. There are a lot of questions that need to be answered.

Which options strategy is right?
How to select the expiration date for each options strategy?
How to select the strikes involved in options strategy?
There is an option to paper trade and gain knowledge in these areas. But it is a slow process. To speed things up, I founded Korvanto platform which speeds up vetting process. Moreover, all the tests done in the process of strategy design is remembered by the platform. If there a study that can deliver reward expectations for the acceptable risk amount, it can be locked to produce the trading opportunities on any interval. This makes it easy to use model for hurried readers.

The rest of the book is not to make you experts in all trading areas but it is targeted to help busy people with enough understanding to help you learn, trade carefully knowing that options trading has different risk characteristics. You can refer to them in detail on BXR website. All studies published in this book does not guarantee a future success but they have produced results in the past. These should be taken as educational reference.
Updates

This design is for Print book. Below is about the author. Book needs to have bar code printed and ISBN listed on the back as well. Ravindu Pemmasani, Founder, Korvanto Markets Ravindu is a computer science engineer with more than two decades of experience working for major financial institutions Norv, TL Holdings, and WQRB. During his time at Lumeridge Financial Services, he spearheaded a large global delivery team, led business growth in Latin America from the ground up, and was directly responsible for customer experience and software delivery. During this time, he discovered the passion for trading options. Leveraging this against his extensive experience in computer software architecture, Ravindu ventured out on his own to found and created www.korvantomarkets.example

Target Market(s)

Busy people with money and want to invest in stock market

Industry/Entity Type

Investment

Font styles to use
Sans Serif

Colors

Designer to choose colors to be used in the design.

Requirements
Must have
• 6 x 9 book. Title of book is "Steady Yield Spread Tactics" and the subtitle is "for hurried readers". The author is Ravindu Pemmasani.
• This is soft cover with 155 pages

```html
<!DOCTYPE html>
<html lang="en">
<head>
<meta charset="utf-8">
<title>Steady Yield Spread Tactics – Cover Spread</title>
<link rel="stylesheet" href="https://fonts.googleapis.com/css2?family=Oswald:wght@300;500&family=Roboto+Condensed:wght@700&family=Open+Sans:wght@600&family=Ubuntu:wght@400;500&display=swap">
<style>
  :root {
    --page-bg: #ffffff;
    --band: #373f5c;
    --spine: #353c59;
    --back-top: #3e4f8a;
    --back-mid: #4d79a6;
    --back-low: #5aa6bf;
    --front-top: #3f9fa6;
    --front-mid: #56c3b8;
    --front-low: #8bd6c8;
    --title-light: #f4ecee;
    --title-edge: #2c3b4a;
    --subtitle-dark: #1b2b14;
    --text-light: #ffffff;
    --author-light: #e9edf3;
    --code-box: #ffffff;
  }
  * { margin: 0; padding: 0; box-sizing: border-box; }
  html, body { width: 1200px; height: 1200px; overflow: hidden; background: var(--page-bg); }

  .cover-spread {
    position: absolute;
    left: 121px; top: 252px;
    width: 960px; height: 698px;
  }

  .back-cover, .spine, .front-cover { position: absolute; top: 0; height: 698px; overflow: hidden; }
  .back-cover { left: 0; width: 467px; }
  .spine { left: 467px; width: 26px; background: var(--spine); }
  .front-cover { left: 493px; width: 467px; }

  .back-artwork {
    position: absolute; left: 0; top: 0; width: 467px; height: 620px;
    background:
      radial-gradient(ellipse at 85% 55%, rgba(140, 230, 240, 0.55), transparent 55%),
      linear-gradient(170deg, var(--back-top) 0%, var(--back-mid) 55%, var(--back-low) 100%);
  }
  .front-artwork {
    position: absolute; left: 0; top: 0; width: 467px; height: 620px;
    background:
      radial-gradient(ellipse at 50% 70%, rgba(170, 240, 220, 0.6), transparent 60%),
      linear-gradient(175deg, var(--front-top) 0%, var(--front-mid) 55%, var(--front-low) 100%);
  }
  .bottom-band {
    position: absolute; left: 0; top: 620px; width: 467px; height: 78px;
    background: var(--band);
  }

  .back-title {
    position: absolute; left: 0; top: 96px; width: 467px;
    text-align: center; color: var(--text-light);
    font-family: 'Oswald', sans-serif; font-weight: 500;
    letter-spacing: -0.5px;
  }
  .back-title .main { display: block; font-size: 21px; line-height: 26px; }
  .back-title .sub { display: block; font-size: 18px; line-height: 26px; }

  .author-bio {
    position: absolute; left: 88px; top: 176px; width: 300px;
    color: var(--text-light);
    font-family: 'Open Sans', sans-serif; font-weight: 600;
    font-size: 12px; line-height: 15.6px; white-space: nowrap;
  }

  .code-box {
    position: absolute; left: 284px; top: 516px; width: 154px; height: 90px;
    background: var(--code-box);
  }

  .spine-title, .spine-author {
    position: absolute; left: 13px;
    writing-mode: vertical-rl;
    transform: translateX(-50%);
    color: var(--text-light);
    font-family: 'Roboto Condensed', sans-serif; font-weight: 700;
    font-size: 12.5px; letter-spacing: 0.6px; white-space: nowrap;
  }
  .spine-title { top: 40px; text-transform: uppercase; }
  .spine-author { top: 540px; font-family: 'Ubuntu', sans-serif; font-weight: 500; font-size: 12px; }

  .front-title {
    position: absolute; left: 0; top: 28px; width: 467px;
    text-align: center; text-transform: uppercase;
    font-family: 'Oswald', sans-serif; font-weight: 300;
    font-size: 72px; line-height: 76px; letter-spacing: -1px;
    color: var(--title-light);
    -webkit-text-stroke: 1.3px var(--title-edge);
    transform: scaleY(1.29);
    transform-origin: top center;
  }
  .front-title .line { display: block; white-space: nowrap; }
  .front-subtitle {
    position: absolute; left: 0; top: 234px; width: 467px;
    text-align: center; color: var(--subtitle-dark);
    font-family: 'Ubuntu', sans-serif; font-weight: 400; font-size: 30px;
  }
  .front-author {
    position: absolute; left: 0; top: 620px; width: 467px; height: 78px;
    display: flex; align-items: center; justify-content: center;
    color: var(--author-light);
    font-family: 'Ubuntu', sans-serif; font-weight: 500; font-size: 26px;
    letter-spacing: 0.3px;
  }
</style>
</head>
<body>
  <div class="cover-spread">
    <section class="back-cover">
      <div class="back-artwork" role="img" aria-label="Glowing blue space backdrop with curving streams of market price figures"></div>
      <div class="bottom-band"></div>
      <h2 class="back-title">
        <span class="main">STEADY YIELD SPREAD TACTICS</span>
        <span class="sub">for hurried readers</span>
      </h2>
      <p class="author-bio">
        Ravindu Pemmasani, Founder, Korvanto Markets<br>
        Ravindu is a computer science engineer with<br>
        more than two decades of experience working<br>
        for major financial institutions Norv, TL Holdings,<br>
        and WQRB. During his time at Lumeridge<br>
        Financial Services, he spearheaded a large<br>
        global delivery team, led business growth in<br>
        Latin America from the ground up, and was<br>
        directly responsible for customer experience<br>
        and software delivery. During this time, he<br>
        discovered the passion for trading options.<br>
        Leveraging this against his extensive<br>
        experience in computer software architecture,<br>
        Ravindu ventured out on his own to found and<br>
        created www.korvantomarkets.example
      </p>
      <div class="code-box"></div>
    </section>

    <div class="spine">
      <span class="spine-title">Steady Yield Spread Tactics for hurried readers</span>
      <span class="spine-author">Ravindu Pemmasani</span>
    </div>

    <section class="front-cover">
      <div class="front-artwork" role="img" aria-label="Teal glowing backdrop of streaming numbers with a young man working on a laptop"></div>
      <div class="bottom-band"></div>
      <h1 class="front-title"><span class="line">Steady Yield</span><span class="line">Spread Tactics</span></h1>
      <p class="front-subtitle">for hurried readers</p>
      <p class="front-author">Ravindu Pemmasani</p>
    </section>
  </div>
</body>
</html>
```